MCDI Root Beer bottle label design.

We produce homemade root beer the same way since 1965. Family owned and third generation owner. The root beer will bring you back 50 years. This will go on a brown beer bottle. Our website is www.marburycreekdrivein.example. We have a logo on our website but I would like something different. we are a 50's style drive in restaurant like J&P and Vireo. I would like this to be a new logo for our business.

Target Market(s)

All ages

Colors
f37122
ffffff
000000

Requirements
Must have
• Easy to read. Retro style font with a lot of white in the logo. I would like to be able to pull the logo out separately and put that just on the bottle if I choose. I added some examples of labels and the style of font I like.

```html
<!DOCTYPE html>
<html lang="en">
<head>
<meta charset="utf-8">
<title>Marbury Creek No.1 Root Beer Label</title>
<link rel="stylesheet" href="https://fonts.googleapis.com/css2?family=Alfa+Slab+One&family=Oswald:wght@400;600&family=Yellowtail&display=swap">
<style>
  :root {
    --bg: #0b0b0b;
    --label-red: #6e1614;
    --label-red-dark: #551010;
    --gold: #e0a02a;
    --orange: #f37122;
    --white: #ffffff;
    --soft-white: #ece6dc;
  }
  * { margin: 0; padding: 0; box-sizing: border-box; }
  html, body { width: 1200px; height: 960px; overflow: hidden; background: var(--bg); }
  .canvas { position: relative; width: 1200px; height: 960px; background: var(--bg); }

  .label {
    position: absolute; left: 390px; top: 110px; width: 560px; height: 620px;
    background: radial-gradient(ellipse at 50% 40%, var(--label-red), var(--label-red-dark));
    border-radius: 6px;
  }
  .label-frame { position: absolute; inset: 0; }

  .tagline {
    position: absolute; top: 70px; font-family: "Oswald", sans-serif; font-weight: 600;
    font-size: 15px; letter-spacing: 2px; color: var(--gold); text-transform: uppercase;
    border-top: 1px solid var(--gold); border-bottom: 1px solid var(--gold); padding: 2px 4px;
  }
  .tagline--left { left: 70px; }
  .tagline--right { right: 70px; }

  .car-illustration {
    position: absolute; left: 225px; top: 44px; width: 110px; height: 66px;
    border-radius: 30px 30px 10px 10px;
    background: linear-gradient(180deg, #9a6a22, #6e4a18);
  }

  .brand-name {
    position: absolute; left: 0; right: 0; text-align: center;
    font-family: "Alfa Slab One", serif; color: var(--white); line-height: 1;
  }
  .brand-name--top { top: 140px; font-size: 84px; letter-spacing: 1px; }
  .brand-name--bottom { top: 232px; font-size: 64px; letter-spacing: 4px; }

  .number-row {
    position: absolute; top: 318px; left: 0; right: 0; display: flex;
    justify-content: center; align-items: center; gap: 18px;
  }
  .number-row .rule { width: 110px; height: 2px; background: var(--gold); }
  .number {
    font-family: "Oswald", sans-serif; font-weight: 600; font-size: 44px; color: var(--soft-white);
  }

  .product-name {
    position: absolute; top: 380px; left: 0; right: 0; text-align: center;
    font-family: "Yellowtail", cursive; font-size: 92px; color: var(--soft-white); line-height: 1;
  }

  .ribbon { position: absolute; left: 120px; top: 488px; width: 320px; height: 50px; }
  .ribbon-text {
    position: absolute; left: 0; right: 0; top: 494px; text-align: center;
    font-family: "Oswald", sans-serif; font-weight: 600; font-size: 28px; letter-spacing: 4px;
    color: var(--soft-white);
  }
  .since {
    position: absolute; left: 0; right: 0; top: 546px; text-align: center;
    font-family: "Oswald", sans-serif; font-size: 17px; letter-spacing: 3px; color: var(--soft-white);
  }
  .website {
    position: absolute; left: 0; right: 0; top: 574px; text-align: center;
    font-family: "Oswald", sans-serif; font-size: 12px; letter-spacing: 1.5px; color: var(--gold);
    text-transform: uppercase;
  }

  .standalone-logo {
    position: absolute; left: 70px; top: 760px; width: 420px; text-align: center;
    font-family: "Alfa Slab One", serif; color: var(--white); line-height: 1;
  }
  .standalone-logo .line-top { display: block; font-size: 60px; }
  .standalone-logo .line-bottom { display: block; font-size: 52px; letter-spacing: 4px; margin-top: 8px; }
</style>
</head>
<body>
<main class="canvas">
  <section class="label">
    <svg class="label-frame" width="560" height="620" viewBox="0 0 560 620" aria-hidden="true">
      <rect x="14" y="14" width="532" height="592" fill="none" stroke="var(--gold)" stroke-width="2.5"/>
      <rect x="22" y="22" width="516" height="576" fill="none" stroke="var(--gold)" stroke-width="1" stroke-dasharray="3 3"/>
    </svg>

    <span class="tagline tagline--left">Will bring you</span>
    <div class="car-illustration" role="img" aria-label="Vintage 1950s car illustration"></div>
    <span class="tagline tagline--right">Back 50 years</span>

    <div class="brand-name brand-name--top">MARBURY</div>
    <div class="brand-name brand-name--bottom">CREEK</div>

    <div class="number-row">
      <span class="rule"></span>
      <span class="number">№1</span>
      <span class="rule"></span>
    </div>

    <div class="product-name">root beer</div>

    <svg class="ribbon" viewBox="0 0 320 50" aria-hidden="true">
      <polygon points="0,10 30,10 30,46 0,46 12,28" fill="none" stroke="var(--gold)" stroke-width="2"/>
      <polygon points="320,10 290,10 290,46 320,46 308,28" fill="none" stroke="var(--gold)" stroke-width="2"/>
      <rect x="22" y="2" width="276" height="40" fill="var(--label-red-dark)" stroke="var(--gold)" stroke-width="2"/>
    </svg>
    <div class="ribbon-text">HOMEMADE</div>
    <div class="since">— SINCE 1965 —</div>
    <div class="website">www.marburycreekdrivein.example</div>
  </section>

  <div class="standalone-logo">
    <span class="line-top">MARBURY</span>
    <span class="line-bottom">CREEK</span>
  </div>
</main>
</body>
</html>
```